Stationery Design for a fast food resturaunt

We just created our logo, we need nice stationary to go with it. We beed the design to be on white background and black background.

Target Market(s)

Landlords who will lease their retail shops to us. Shopping Mall Management.Real Estate Professionals.

Font styles to use
Sans Serif

```html
<!DOCTYPE html>
<html lang="en">
<head>
<meta charset="utf-8">
<title>Amber Hive — Business Cards</title>
<link rel="stylesheet" href="https://fonts.googleapis.com/css2?family=Mulish:wght@400;700;800&display=swap">
<style>
  :root {
    --backdrop: #e4e4e9;
    --charcoal: #3f3f41;
    --paper: #fbfbfc;
    --gold: #e6a915;
    --ink: #3a3a3c;
    --white: #ffffff;
  }
  * { box-sizing: border-box; margin: 0; padding: 0; }
  html, body {
    width: 1200px;
    height: 934px;
    overflow: hidden;
  }
  body {
    background: var(--backdrop);
    font-family: "Mulish", sans-serif;
    position: relative;
  }
  .card {
    position: absolute;
    width: 620px;
    height: 354px;
    overflow: hidden;
    box-shadow: 0 6px 18px rgba(0,0,0,0.12);
  }
  .card--back { left: 290px; top: 70px; background: var(--charcoal); }
  .card--front { left: 290px; top: 480px; background: var(--paper); }

  .wordmark {
    position: absolute;
    display: flex;
    align-items: center;
    gap: 12px;
    font-weight: 400;
    font-size: 34px;
    letter-spacing: 3px;
    text-transform: uppercase;
    line-height: 1;
  }
  .wordmark__square {
    width: 18px;
    height: 18px;
    background: var(--gold);
  }
  .card--back .wordmark { right: 46px; top: 40px; color: var(--white); }
  .card--front .wordmark { left: 52px; top: 120px; color: var(--ink); }

  .edge-blocks {
    position: absolute;
    display: flex;
    flex-direction: column;
    gap: 16px;
  }
  .edge-blocks span { display: block; width: 30px; height: 20px; }
  .card--back .edge-blocks { left: 0; top: 150px; }
  .card--back .edge-blocks span { background: var(--white); }
  .card--back .edge-blocks span.is-gold { background: var(--gold); }
  .card--front .edge-blocks { right: 0; top: 110px; gap: 22px; }
  .card--front .edge-blocks span { width: 34px; height: 26px; background: var(--charcoal); }
  .card--front .edge-blocks span.is-gold { background: var(--gold); }

  .holder {
    position: absolute;
    right: 58px;
    top: 40px;
    text-align: right;
  }
  .holder__name {
    color: var(--gold);
    font-weight: 800;
    font-size: 18px;
    letter-spacing: 0.5px;
    text-transform: uppercase;
  }
  .holder__role {
    color: var(--ink);
    font-size: 14px;
    margin-top: 2px;
  }

  .contact {
    position: absolute;
    left: 52px;
    bottom: 38px;
    color: var(--ink);
    font-size: 14px;
    line-height: 1.5;
  }
  .contact__label { color: var(--gold); font-weight: 700; }
</style>
</head>
<body>
  <section class="card card--back" aria-label="Business card, dark side">
    <div class="wordmark"><span class="wordmark__square"></span>Amber Hive</div>
    <div class="edge-blocks">
      <span></span><span class="is-gold"></span><span></span>
    </div>
  </section>

  <section class="card card--front" aria-label="Business card, white side">
    <div class="holder">
      <p class="holder__name">Jordan Mercer</p>
      <p class="holder__role">Managing Director</p>
    </div>
    <div class="wordmark"><span class="wordmark__square"></span>Amber Hive</div>
    <div class="edge-blocks">
      <span></span><span class="is-gold"></span><span></span>
    </div>
    <address class="contact" style="font-style:normal">
      <p>18 Willow Court, Fairview, CA 90412</p>
      <p><span class="contact__label">T:</span> +61 800-555-0142 · <span class="contact__label">E:</span> info@amberhive.com · <span class="contact__label">W:</span> www.amberhive.com</p>
    </address>
  </section>
</body>
</html>
```